Brindle Works - Fast, Efficient and Gas Mainteance for Domestic, Commercial and Industrial clients

We are in the process of purchasing a new business and would like to get a new logo and business card.
Business is a gas maintenance business that also does new gas installations.
Has been established since 1988.
Services include:
Install all types of gas appliances & equipment inc. hot water units
Maintain / repair / replace all types of gas appliances & equipment

Target Market(s)

Domestic, Commercial and Industrial clients

Industry/Entity Type

Business

Contact Information for Business Card

admin@brindleworks-example.com.au
07 5981 4726
Brindle Works PTY LTD

Logo Text

Gas Fitting & Plumbing Maintenance Specialists

Font styles to use
Sans Serif

Requirements
Must have
• Logo
• Business name, contact number, email address, web address
• Domestic | Commercial | Industrial Est Since 1988
Nice to have
• Possibly a black card with a flame logo to one side
Should not have
• Spelling errors

```html
<!DOCTYPE html>
<html lang="en">
<head>
<meta charset="utf-8">
<title>Brindle Works PTY LTD – Business Card</title>
<link rel="stylesheet" href="https://fonts.googleapis.com/css2?family=Quicksand:wght@500;600;700&display=swap">
<style>
  :root {
    --page-bg: #ecebe8;
    --card-top: #f3f1ee;
    --card-bottom: #e6e2dd;
    --band-dark: #262626;
    --band-mid: #3a3a3a;
    --accent-line: #c8532a;
    --ink: #2b2b2b;
    --ink-soft: #3c3c3c;
    --flame-red: #d8482a;
    --flame-orange: #e5862e;
    --flame-yellow: #e9cf34;
    --mark-fill: #ece6dc;
  }
  * { margin: 0; padding: 0; box-sizing: border-box; }
  html, body { width: 1200px; height: 970px; overflow: hidden; }
  body {
    background: var(--page-bg);
    font-family: "Quicksand", sans-serif;
    position: relative;
  }
  .business-card {
    position: absolute;
    left: 80px; top: 190px;
    width: 1040px; height: 590px;
    background: linear-gradient(160deg, var(--card-top), var(--card-bottom));
    box-shadow: 0 10px 30px rgba(0,0,0,.18);
    overflow: hidden;
  }
  .side-band {
    position: absolute; left: 0; top: 0;
    width: 152px; height: 100%;
    background: linear-gradient(180deg, var(--band-mid), var(--band-dark));
  }
  .accent-rule {
    position: absolute; left: 155px; top: 0;
    width: 2px; height: 100%;
    background: var(--accent-line);
  }
  .brand-mark {
    position: absolute; left: 55px; top: 60px;
    width: 180px; height: 180px;
    border-radius: 50%;
    background: var(--mark-fill);
    border: 6px solid var(--band-dark);
  }
  .company-name {
    position: absolute; left: 252px; top: 125px;
    font-size: 41px; font-weight: 500; color: var(--ink);
    letter-spacing: .5px; white-space: nowrap;
  }
  .company-tagline {
    position: absolute; left: 255px; top: 174px;
    font-size: 17.5px; font-weight: 600; color: var(--ink);
    letter-spacing: 1.3px; white-space: nowrap;
  }
  .flame-art {
    position: absolute; right: 0; bottom: 0;
    width: 290px; height: 400px;
    background: radial-gradient(ellipse at 60% 80%, var(--flame-yellow) 0%, var(--flame-orange) 40%, rgba(216,72,42,.55) 65%, rgba(216,72,42,0) 80%);
  }
  .employee-name {
    position: absolute; left: 256px; top: 333px;
    font-size: 36px; font-weight: 700; color: var(--ink);
  }
  .address {
    position: absolute; left: 258px; top: 396px;
    font-size: 27px; font-weight: 500; color: var(--ink-soft); line-height: 34px;
  }
  .contact-list {
    position: absolute; left: 258px; top: 475px;
    list-style: none;
    font-size: 27px; font-weight: 500; color: var(--ink-soft);
  }
  .contact-list li { display: flex; align-items: center; gap: 14px; height: 36px; }
  .contact-list svg { width: 27px; height: 27px; flex: none; }
</style>
</head>
<body>
  <div class="business-card">
    <div class="side-band"></div>
    <div class="accent-rule"></div>
    <div class="brand-mark"></div>

    <div class="company-name">Brindle Works PTY LTD</div>
    <div class="company-tagline">Domestic | Commercial | Industrial Est Since 1988</div>

    <div class="flame-art" role="img" aria-label="Flame illustration in red, orange and yellow"></div>

    <div class="employee-name">Employee Name</div>
    <div class="address">0000 your address Avenue<br>Sioux Falls, SD 0000</div>

    <ul class="contact-list">
      <li>
        <svg viewBox="0 0 24 24" aria-hidden="true">
          <rect x="1" y="1" width="22" height="22" fill="#3a3a3a"/>
          <path d="M5 9c0-2 3-3 7-3s7 1 7 3v1h-3V8.5h-8V10H5z M7 11h10l1 7H6z" fill="#ecebe8"/>
          <circle cx="12" cy="14.5" r="1.8" fill="#3a3a3a"/>
        </svg>
        <span>07 5981 4726</span>
      </li>
      <li>
        <svg viewBox="0 0 24 24" aria-hidden="true">
          <rect x="1" y="1" width="22" height="22" fill="#3a3a3a"/>
          <rect x="5" y="7" width="14" height="10" fill="none" stroke="#ecebe8" stroke-width="1.6"/>
          <path d="M5 7l7 6 7-6 M5 17l5-5 M19 17l-5-5" fill="none" stroke="#ecebe8" stroke-width="1.6"/>
        </svg>
        <span>admin@brindleworks-example.com.au</span>
      </li>
    </ul>
  </div>
</body>
</html>
```